Real Estate "For Sale" Sign for construction company

We need a sign that we can use to hang on a post and place on the road when we sell a property. The sign will be simple and will need to mainly feature our logo (files attached), as well as the words "For Sale", and then our phone number "(555) 617 3489". The sign will hang on a post that'll look something like the attached picture.

Target Market(s)

Home buyers

Industry/Entity Type

Real Estate

Font styles to use
Serif
Sans Serif

Colors
0054AA
0677BA
7BADD7
CADEEF
E8F1F8
0094D4
00A9DD
6FCCEA
C7EBF8
E9F6FB

Requirements
Must have
• For Sale & our phone number

```html
<!DOCTYPE html>
<html lang="en">
<head>
<meta charset="utf-8">
<title>Ridgeway Homes – For Sale Sign</title>
<link href="https://fonts.googleapis.com/css2?family=Montserrat:wght@500;700&display=swap" rel="stylesheet">
<style>
  :root {
    --page: #ffffff;
    --sky: #8fd6f5;
    --sky-band: #84cbeb;
    --halo: #c8e9fb;
    --white: #ffffff;
    --navy: #253a7b;
    --brand-blue: #1a7fc4;
    --mark-blue: #6fccea;
  }
  * { margin: 0; padding: 0; box-sizing: border-box; }
  html, body {
    width: 1200px; height: 946px; overflow: hidden;
    background: var(--page);
    font-family: "Montserrat", Arial, sans-serif;
  }
  .sign {
    position: absolute; left: 89px; top: 76px;
    width: 1026px; height: 769px;
    background: var(--white);
    box-shadow: 0 6px 22px rgba(0,0,0,0.28);
    overflow: hidden;
  }
  .sign__sky {
    position: absolute; left: 0; top: 0; width: 1026px; height: 426px;
    background: var(--sky);
    overflow: hidden;
  }
  .sign__stripes { position: absolute; inset: 0; }
  .sign__halo {
    position: absolute; left: 237px; top: 89px;
    width: 534px; height: 534px; border-radius: 50%;
    background: var(--halo);
  }
  .sign__arch {
    position: absolute; left: 256px; top: 109px;
    width: 496px; height: 496px; border-radius: 50%;
    background: var(--white);
  }
  .sign__headline {
    position: absolute; left: 0; right: 0; top: 34px;
    text-align: center;
    font-weight: 700; font-size: 146px; line-height: 1;
    letter-spacing: 2px;
    color: var(--navy);
  }
  .sign__white {
    position: absolute; left: 0; top: 426px; width: 1026px; height: 192px;
    background: var(--white);
  }
  .brand { position: absolute; left: 0; right: 0; top: 300px; text-align: center; }
  .brand__mark {
    display: block; margin: 0 auto;
    width: 124px; height: 124px; border-radius: 50%;
    background: var(--mark-blue);
  }
  .brand__name {
    display: block; margin-top: 30px;
    font-weight: 500; font-size: 84px; line-height: 1;
    color: var(--brand-blue);
  }
  .sign__contact {
    position: absolute; left: 0; top: 618px; width: 1026px; height: 151px;
    background: var(--navy);
    display: flex; align-items: center; justify-content: center; gap: 18px;
  }
  .contact__icon {
    width: 70px; height: 70px; border-radius: 50%;
    background: var(--sky);
    display: flex; align-items: center; justify-content: center;
  }
  .contact__text {
    color: var(--white);
    font-weight: 500; font-size: 70px; line-height: 1;
  }
</style>
</head>
<body>
  <main class="sign">
    <div class="sign__sky">
      <svg class="sign__stripes" width="1026" height="426" viewBox="0 0 1026 426">
        <g fill="var(--sky-band)" opacity="0.55">
          <polygon points="0,20 0,60 300,320 340,320"/>
          <polygon points="0,150 0,190 220,380 260,380"/>
          <polygon points="1026,20 1026,60 726,320 686,320"/>
          <polygon points="1026,150 1026,190 806,380 766,380"/>
        </g>
      </svg>
      <div class="sign__halo"></div>
      <div class="sign__arch"></div>
      <h1 class="sign__headline">FOR SALE</h1>
    </div>
    <div class="sign__white"></div>
    <div class="brand">
      <span class="brand__mark"></span>
      <span class="brand__name">Ridgeway Homes</span>
    </div>
    <div class="sign__contact">
      <span class="contact__icon">
        <svg width="40" height="40" viewBox="0 0 24 24" aria-hidden="true">
          <path fill="var(--navy)" d="M6.6 10.8a15.1 15.1 0 0 0 6.6 6.6l2.2-2.2c.3-.3.7-.4 1-.2 1.1.4 2.3.6 3.6.6.6 0 1 .4 1 1V20c0 .6-.4 1-1 1A17 17 0 0 1 3 4c0-.6.4-1 1-1h3.5c.6 0 1 .4 1 1 0 1.3.2 2.5.6 3.6.1.3 0 .7-.2 1z"/>
          <path fill="none" stroke="var(--navy)" stroke-width="1.6" stroke-linecap="round" d="M14 6.5a4 4 0 0 1 3.5 3.5M14 3a7.5 7.5 0 0 1 7 7"/>
        </svg>
      </span>
      <span class="contact__text">Call us (555) 617 3489</span>
    </div>
  </main>
</body>
</html>
```